Letterhead & Email Signature Design

Kindly assist redesign this letterhead as well as the Email signature. I have uploaded the current designs that needs some new look

```html
<!DOCTYPE html>
<html lang="en">
<head>
<meta charset="utf-8">
<title>Ridgeway Baloyi Inc – Stationery</title>
<link href="https://fonts.googleapis.com/css2?family=Poppins:wght@300;400;600;700&display=swap" rel="stylesheet">
<style>
  :root {
    --ink: #000000;
    --paper: #ffffff;
    --stone: #6b6b6b;
    --text: #1a1a1a;
  }
  * { margin: 0; padding: 0; box-sizing: border-box; }
  html, body { width: 1200px; height: 1085px; overflow: hidden; background: var(--paper); }
  body { position: relative; font-family: "Poppins", sans-serif; color: var(--text); }

  /* Letterhead */
  .letterhead {
    position: absolute; left: 416px; top: 102px; width: 678px; height: 875px;
    border: 1px solid var(--ink); background: var(--paper);
  }
  .letterhead__band { position: absolute; left: 0; top: 0; width: 100%; height: 80px; background: var(--ink); }
  .letterhead__foot { position: absolute; left: 0; bottom: 0; width: 100%; height: 9px; background: var(--ink); }
  .letterhead__mark {
    position: absolute; left: 26px; top: 27px; width: 100px; height: 100px; border-radius: 50%;
    background: var(--stone); display: flex; align-items: center; justify-content: center; text-align: center;
  }
  .letterhead__mark span { color: var(--paper); font-weight: 700; font-size: 10px; line-height: 1.2; letter-spacing: .5px; }
  .letterhead__contacts { position: absolute; left: 457px; top: 18px; list-style: none; }
  .letterhead__contacts li { display: flex; align-items: center; gap: 6px; height: 17px; color: var(--paper); font-size: 11.5px; font-weight: 300; }

  /* Business card */
  .card {
    position: absolute; left: 103px; top: 386px; width: 665px; height: 356px;
    border: 1px solid var(--ink); background: var(--paper); overflow: hidden;
  }
  .card__band { position: absolute; left: 0; top: 0; width: 100%; height: 188px; background: var(--ink); }
  .card__mark {
    position: absolute; left: 59px; top: 85px; width: 220px; height: 202px; border-radius: 50%;
    background: var(--stone); display: flex; align-items: center; justify-content: center; text-align: center;
  }
  .card__mark span { color: var(--paper); font-weight: 700; font-size: 19px; line-height: 1.25; letter-spacing: .5px; }
  .card__name { position: absolute; left: 364px; top: 69px; color: var(--paper); font-weight: 700; font-size: 19px; letter-spacing: .6px; }
  .card__role { position: absolute; left: 364px; top: 93px; color: var(--paper); font-weight: 300; font-size: 10px; letter-spacing: 16px; }
  .card__lockup { position: absolute; left: 364px; top: 126px; display: flex; color: var(--paper); }
  .card__lockup div { display: flex; flex-direction: column; }
  .card__lockup strong { font-weight: 600; font-size: 17px; letter-spacing: .6px; line-height: 1.1; }
  .card__lockup small { font-weight: 300; font-size: 9px; letter-spacing: 2.5px; }
  .card__lockup .left { align-items: flex-end; padding-right: 10px; border-right: 1.5px solid var(--paper); }
  .card__lockup .right { padding-left: 10px; }
  .card__contacts { position: absolute; left: 364px; top: 215px; list-style: none; }
  .card__contacts li { display: flex; align-items: flex-start; gap: 8px; font-size: 11px; font-weight: 300; line-height: 15px; margin-bottom: 3px; }
  .card__contacts li.gap { margin-bottom: 12px; }
  .icon { flex: none; width: 11px; height: 11px; margin-top: 2px; }
  .letterhead__contacts .icon { margin-top: 0; }
</style>
</head>
<body>

<section class="letterhead" aria-label="Letterhead">
  <div class="letterhead__band"></div>
  <div class="letterhead__mark"><span>RIDGEWAY<br>BALOYI</span></div>
  <ul class="letterhead__contacts">
    <li><svg class="icon" viewBox="0 0 12 12"><circle cx="6" cy="6" r="6" fill="#fff"/><path d="M4 3.2l1 1.4-.6.7c.4.9 1.1 1.6 2 2l.7-.6 1.4 1-.5 1C5.7 8.5 3.5 6.3 3.3 4z" fill="#000"/></svg>+27 12 555 0148</li>
    <li><svg class="icon" viewBox="0 0 12 12"><circle cx="6" cy="6" r="6" fill="#fff"/><rect x="3" y="4" width="6" height="4.2" fill="#000"/><path d="M3 4l3 2.3L9 4" stroke="#fff" stroke-width=".7" fill="none"/></svg>Lerato@Ridgewaybaloyi.co.za</li>
    <li><svg class="icon" viewBox="0 0 12 12"><circle cx="6" cy="6" r="6" fill="#fff"/><circle cx="6" cy="6" r="3" fill="none" stroke="#000" stroke-width=".8"/><path d="M3 6h6M6 3v6" stroke="#000" stroke-width=".7"/></svg>www.ridgewaybaloyiinc.co.za</li>
  </ul>
  <div class="letterhead__foot"></div>
</section>

<section class="card" aria-label="Business card">
  <div class="card__band"></div>
  <div class="card__mark"><span>RIDGEWAY<br>BALOYI</span></div>
  <p class="card__name">LERATO NKOSI</p>
  <p class="card__role">DIRECTOR</p>
  <div class="card__lockup">
    <div class="left"><strong>BALOYI</strong><small>INC</small></div>
    <div class="right"><strong>RIDGEWAY</strong><small>EST. 2014</small></div>
  </div>
  <ul class="card__contacts">
    <li class="gap"><svg class="icon" viewBox="0 0 12 12"><circle cx="6" cy="6" r="6" fill="#000"/><circle cx="6" cy="5.2" r="1.6" fill="#fff"/></svg>41 Acacia Lane, The Grove</li>
    <li class="gap"><svg class="icon" viewBox="0 0 12 12"><circle cx="6" cy="6" r="6" fill="#000"/><circle cx="6" cy="5.2" r="1.6" fill="#fff"/></svg>Riverside Centre, First Floor, Block C,<br>8 Marula Street, Fern Hill, Mokopane</li>
    <li><svg class="icon" viewBox="0 0 12 12"><circle cx="6" cy="6" r="6" fill="#000"/><path d="M4 3.2l1 1.4-.6.7c.4.9 1.1 1.6 2 2l.7-.6 1.4 1-.5 1C5.7 8.5 3.5 6.3 3.3 4z" fill="#fff"/></svg>+27 12 555 0148</li>
    <li><svg class="icon" viewBox="0 0 12 12"><circle cx="6" cy="6" r="6" fill="#000"/><rect x="3" y="4" width="6" height="4.2" fill="#fff"/><path d="M3 4l3 2.3L9 4" stroke="#000" stroke-width=".7" fill="none"/></svg>Lerato@Ridgewaybaloyi.co.za</li>
    <li><svg class="icon" viewBox="0 0 12 12"><circle cx="6" cy="6" r="6" fill="#000"/><circle cx="6" cy="6" r="3" fill="none" stroke="#fff" stroke-width=".8"/><path d="M3 6h6M6 3v6" stroke="#fff" stroke-width=".7"/></svg>www.ridgewaybaloyiinc.co.za</li>
  </ul>
</section>

</body>
</html>
```